Diesel Fitting/Mechanical Company Needs a new Business Card

We would like a new business card that showcases our logo and business information.

Industry/Entity Type

Business

Contact Information for Business Card

314 Wendale Street
PO Box 7581 KELBURN DOWNS QLD 4790
Phone: 49312787 Fax: 49312688 Mobile: 0438915276 ABN: 63 519 087 342

Requirements
Must have
• The following email addresses:
• admin@tkservicing.com.au , sales@tkservicing.com.au , accounts@tkservicing.com.au , parts@tkservicing.com.au , office@tkservicing.com.au
• Also need to have the website: www.tkservicing.com.au

```html
<!DOCTYPE html>
<html lang="en">
<head>
<meta charset="utf-8">
<title>TK Servicing – Business Card</title>
<link rel="stylesheet" href="https://fonts.googleapis.com/css2?family=Exo+2:wght@400;600&display=swap">
<style>
  :root {
    --bg: #e9e6e2;
    --card: #070707;
    --orange: #f07a22;
    --white: #f2f2f2;
    --rule: #6b6b6b;
  }
  * { box-sizing: border-box; margin: 0; padding: 0; }
  html, body { width: 1200px; height: 1200px; overflow: hidden; }
  body {
    background: var(--bg);
    font-family: "Exo 2", Arial, sans-serif;
    color: var(--white);
    position: relative;
  }
  .card {
    position: absolute;
    left: 120px;
    width: 960px;
    height: 549px;
    background: var(--card);
    box-shadow: 0 6px 18px rgba(0,0,0,0.18);
  }
  .card-back { top: 34px; }
  .card-front { top: 617px; }

  .brand {
    display: flex;
    align-items: center;
    gap: 18px;
    font-weight: 600;
    color: var(--orange);
    white-space: nowrap;
  }
  .brand-dot {
    border-radius: 50%;
    background: var(--orange);
    flex: none;
  }

  /* back */
  .card-back .brand {
    position: absolute;
    top: 140px;
    left: 0; right: 0;
    justify-content: center;
    font-size: 64px;
  }
  .card-back .brand-dot { width: 44px; height: 44px; }
  .email-block {
    position: absolute;
    left: 60px; right: 60px;
    bottom: 54px;
    text-align: right;
    font-size: 21px;
    letter-spacing: 0.3px;
    white-space: nowrap;
  }
  .email-line { padding: 12px 0; }
  .email-rule { height: 1px; background: var(--rule); }

  /* front */
  .card-front .brand {
    position: absolute;
    left: 60px;
    top: 236px;
    font-size: 54px;
  }
  .card-front .brand-dot { width: 38px; height: 38px; }
  .contact {
    position: absolute;
    left: 480px;
    top: 96px;
    font-size: 22px;
    line-height: 1.5;
    white-space: nowrap;
  }
  .contact-group {
    border-left: 2px solid var(--orange);
    padding-left: 22px;
    margin-bottom: 26px;
  }
  .label {
    color: var(--orange);
    display: inline-block;
    width: 40px;
  }
</style>
</head>
<body>

<section class="card card-back">
  <div class="brand"><span class="brand-dot"></span>TK Servicing</div>
  <div class="email-block">
    <p class="email-line">parts@tkservicing.com.au | office@tkservicing.com.au</p>
    <div class="email-rule"></div>
    <p class="email-line">admin@tkservicing.com.au | accounts@tkservicing.com.au | sales@tkservicing.com.au</p>
    <div class="email-rule"></div>
  </div>
</section>

<section class="card card-front">
  <div class="brand"><span class="brand-dot"></span>TK Servicing</div>
  <div class="contact">
    <div class="contact-group">
      <p><span class="label">T :</span>49312787</p>
      <p><span class="label">M :</span>0438915276</p>
    </div>
    <div class="contact-group">
      <p><span class="label">F :</span>49312688</p>
      <p><span class="label">W :</span>www.tkservicing.com.au</p>
    </div>
    <div class="contact-group">
      <p>314 Wendale Street</p>
      <p>PO Box 7581 KELBURN DOWNS QLD 4790</p>
    </div>
  </div>
</section>

</body>
</html>
```